Mortgage Broking boutique Business

I’m wanting a revamped look to my existing business card design. I do like the black and silver but happy to have other colours introduced based on your creation. I’ve attached a copy of my current card so you can have a starting point updated details noted brloe. I deal with high net worth individuals so need my card to be sophisticated, classy that gives off a classy vibe

Target Market(s)

High net worth, wealthy

Industry/Entity Type

Mortgage Brokerage

Contact Information for Business Card

Job title: Finance Executive
Phone: +61 7 3287 4419
Mobile: 0471 352 608
Email: marcus@quillbrookcapital.com.au
Web: www.quillbrookcapital.com.au
Address: level 36 Tindale Court, 58 Harwick St Brisbane QLD 4000

Font styles to use
Other font styles liked:
• Helvetica

Colors

Designer to choose colors to be used in the design.

Requirements
Must have
• Use my existing card design as a starting point

```html
<!DOCTYPE html>
<html lang="en">
<head>
<meta charset="utf-8">
<title>Quillbrook Capital – Business Card</title>
<link rel="stylesheet" href="https://fonts.googleapis.com/css2?family=Arimo:wght@400;500&display=swap">
<style>
  :root {
    --backdrop: #eceef0;
    --card: #171c2c;
    --ink: #ffffff;
    --ink-soft: #d9dce3;
    --silver-dark: #6d7077;
    --silver-mid: #b9bbc0;
    --silver-light: #f4f4f5;
  }
  * { margin: 0; padding: 0; box-sizing: border-box; }
  html, body {
    width: 1200px; height: 1200px; overflow: hidden;
    background: var(--backdrop);
    font-family: "Arimo", "Helvetica Neue", Helvetica, Arial, sans-serif;
    color: var(--ink);
  }
  .card {
    position: absolute;
    left: 237px; width: 703px; height: 401px;
    background: var(--card);
    border-radius: 18px;
    overflow: hidden;
  }
  .card--front { top: 130px; }
  .card--back { top: 688px; }

  .brand-name {
    position: absolute;
    white-space: nowrap;
    font-weight: 400;
    color: var(--ink);
    text-transform: uppercase;
  }
  .card--front .brand-name {
    left: 78px; top: 100px;
    font-size: 18px; letter-spacing: 4px;
  }
  .card--back .brand-name {
    left: 68px; top: 94px;
    font-size: 19px; letter-spacing: 4.5px;
  }

  .silver-band {
    position: absolute;
    left: 0; right: 0; top: 340px; height: 26px;
    background: linear-gradient(180deg, var(--silver-dark) 0%, var(--silver-light) 45%, var(--silver-mid) 70%, var(--silver-dark) 100%);
  }
  .silver-band .web {
    position: absolute; left: 0; width: 100%; text-align: center;
    top: 3px; font-size: 20px; color: var(--ink);
    padding-left: 0;
    text-shadow: 0 0 2px rgba(0,0,0,.35);
  }

  .silver-rule {
    position: absolute;
    left: 393px; right: 0; top: 96px; height: 7px;
    background: linear-gradient(90deg, var(--silver-dark) 0%, var(--silver-light) 30%, var(--silver-mid) 60%, var(--silver-light) 85%, var(--silver-dark) 100%);
  }
  .person {
    position: absolute; left: 393px; top: 120px;
  }
  .person__name { font-size: 25px; letter-spacing: .5px; line-height: 1.1; }
  .person__title { font-size: 21px; color: var(--ink-soft); margin-top: 2px; }

  .contact-list {
    position: absolute; top: 292px;
    list-style: none;
    font-size: 16px; color: var(--ink-soft);
  }
  .contact-list--left { left: 68px; }
  .contact-list--right { left: 262px; left: 381px; }
  .contact-list li {
    display: flex; align-items: flex-start;
    line-height: 18px; margin-bottom: 9px;
  }
  .contact-list .icon {
    width: 16px; height: 16px; flex: none; margin-right: 7px; margin-top: 1px;
  }
  .contact-list .address-line { display: block; }
</style>
</head>
<body>

<section class="card card--front" aria-label="Card front">
  <div class="brand-name">Quillbrook Capital</div>
  <div class="silver-band"><span class="web">www.quillbrookcapital.com.au</span></div>
</section>

<section class="card card--back" aria-label="Card back">
  <div class="brand-name">Quillbrook Capital</div>
  <div class="silver-rule"></div>
  <div class="person">
    <div class="person__name">MARCUS REDFERN</div>
    <div class="person__title">Finance Executive</div>
  </div>

  <ul class="contact-list contact-list--left">
    <li>
      <svg class="icon" viewBox="0 0 16 16" aria-hidden="true"><circle cx="8" cy="8" r="8" fill="#fff"/><rect x="5.5" y="3.5" width="5" height="9" rx="1" fill="#171c2c"/><rect x="6.5" y="4.8" width="3" height="5.5" fill="#fff"/></svg>
      <span>0471 352 608</span>
    </li>
    <li>
      <svg class="icon" viewBox="0 0 16 16" aria-hidden="true"><circle cx="8" cy="8" r="8" fill="#fff"/><rect x="4" y="5" width="8" height="6" rx=".6" fill="#171c2c"/><path d="M4.3 5.4 8 8.4l3.7-3" fill="none" stroke="#fff" stroke-width=".9"/></svg>
      <span>marcus@quillbrookcapital.com.au</span>
    </li>
    <li>
      <svg class="icon" viewBox="0 0 16 16" aria-hidden="true"><circle cx="8" cy="8" r="8" fill="#fff"/><g fill="none" stroke="#171c2c" stroke-width="1"><circle cx="8" cy="8" r="4.3"/><ellipse cx="8" cy="8" rx="1.8" ry="4.3"/><path d="M3.7 8h8.6"/></g></svg>
      <span>www.quillbrookcapital.com.au</span>
    </li>
  </ul>

  <ul class="contact-list contact-list--right">
    <li>
      <svg class="icon" viewBox="0 0 16 16" aria-hidden="true"><circle cx="8" cy="8" r="8" fill="#fff"/><path d="M5.2 4c.4-.3.9-.2 1.1.2l.8 1.4c.2.4.1.8-.2 1l-.5.4c.4.9 1.1 1.7 2 2.1l.4-.5c.3-.3.7-.4 1-.2l1.4.8c.4.2.5.7.2 1.1l-.6.8c-.4.4-1 .6-1.6.4C7 10.9 5.2 9.1 4.4 6.9c-.2-.6 0-1.2.4-1.6z" fill="#171c2c"/></svg>
      <span>+61 7 3287 4419</span>
    </li>
    <li>
      <svg class="icon" viewBox="0 0 16 16" aria-hidden="true"><circle cx="8" cy="8" r="8" fill="#fff"/><path d="M8 3.4a3 3 0 0 0-3 3c0 2.3 3 5.9 3 5.9s3-3.6 3-5.9a3 3 0 0 0-3-3z" fill="#171c2c"/><circle cx="8" cy="6.4" r="1.1" fill="#fff"/></svg>
      <span>
        <span class="address-line">Level 36 Tindale Court,</span>
        <span class="address-line">58 Harwick St Brisbane QLD 4000</span>
      </span>
    </li>
  </ul>
</section>

</body>
</html>
```